Industrial CNC laser cutting machine manufacturer needs a website designed

We need a website design for our company that re manufactures CNC laser cutting machines, we take old retired machines and completely re manufacture them from the ground up bringing them into the latest technology with all new parts and give them a new lease on life for a fraction of the cost of a new machine.

Machines can be fully customized to suit customers requirements too

My logo will need to be integrated and I want the website to look clean and modern

I will probably want 4 pages,Home, pictures, machines for sale and contact

Coding

Coded - Design and coding required

Number of Pages Required

1 page

```html
<!DOCTYPE html>
<html lang="en">
<head>
<meta charset="utf-8">
<title>Beamforge Machine Works</title>
<link href="https://fonts.googleapis.com/css2?family=Poppins:wght@500;600;700&family=Roboto:wght@400;500;700&display=swap" rel="stylesheet">
<style>
:root{
  --red:#e4132b;
  --dark:#222222;
  --grey-bar:#6d6d6d;
  --footer:#3b3b3b;
  --footer-deep:#222;
  --text:#555;
  --muted:#777;
  --line:#e6e6e6;
}
*{box-sizing:border-box;margin:0;padding:0}
html,body{width:1200px;height:3976px;overflow:hidden}
body{font-family:"Roboto",Arial,sans-serif;color:var(--text);background:#fff;position:relative}
.abs{position:absolute}
.head-font{font-family:"Poppins",Arial,sans-serif}

.topbar{left:0;top:0;width:1200px;height:42px;background:var(--grey-bar);color:#fff;font-size:15px;font-weight:700}
.topbar .social{left:111px;top:15px;display:flex;gap:9px}
.topbar .social span{width:12px;height:12px;border-radius:50%;background:#fff;opacity:.9}
.topbar .phone{left:236px;top:11px;display:flex;align-items:center;gap:10px}
.topbar .links{right:113px;top:13px;display:flex;gap:11px;font-size:13px}

.nav{left:0;top:42px;width:1200px;height:75px;background:#fff;border-bottom:1px solid var(--line)}
.brand{left:111px;top:20px;display:flex;align-items:center;gap:10px;font-family:"Poppins",sans-serif;font-weight:600;font-size:18px;color:var(--red);letter-spacing:.5px}
.brand i{width:22px;height:22px;background:var(--red);display:block}
.menu{left:512px;top:30px;display:flex;gap:26px;font-size:14px;font-weight:700;color:#222}
.menu .on{color:var(--red)}
.search{left:1036px;top:18px;width:44px;height:44px;border-radius:50%;background:var(--red);display:flex;align-items:center;justify-content:center}

.hero{left:0;top:117px;width:1200px;height:521px;background:radial-gradient(ellipse at 75% 45%,#c98a3c 0%,#7a5330 25%,#3d3a3a 55%,#2a2f36 100%)}
.hero h1{left:107px;top:131px;font-family:"Poppins",sans-serif;font-weight:600;font-size:53px;line-height:56px;color:#fff}
.hero p{left:110px;top:259px;width:580px;font-size:14.5px;line-height:26px;color:#fff}
.btn{display:inline-flex;align-items:center;gap:10px;background:var(--red);color:#fff;font-weight:700;font-size:14px}
.hero .btn{left:110px;top:331px;width:155px;height:51px;justify-content:center}

.about-title{left:111px;top:738px;font-family:"Poppins",sans-serif;font-weight:700;font-size:44px;color:#111}
.about-lead{left:111px;top:810px;width:510px;font-size:14px;line-height:27px;color:var(--text)}
.about-body{left:661px;top:746px;width:426px;font-size:14px;line-height:34.3px;color:var(--muted);text-align:justify}
.photo{border:4px solid #fff;box-shadow:0 2px 8px rgba(0,0,0,.25)}
.ph1{left:111px;top:892px;width:488px;height:312px;background:radial-gradient(ellipse at 45% 70%,#d9b070 0%,#5a4330 30%,#1b1c20 75%)}
.ph2{left:520px;top:1042px;width:567px;height:304px;background:radial-gradient(ellipse at 55% 35%,#e3c28a 0%,#9c7a55 40%,#5d4a3e 100%)}

.section-title{left:0;width:1200px;text-align:center;font-family:"Poppins",sans-serif;font-weight:600;font-size:38px;color:#111}
.section-lead{left:260px;width:680px;text-align:center;font-size:14px;line-height:26px;color:var(--muted)}

.cards{left:111px;top:1590px;display:flex;gap:11px}
.card{width:236px;height:281px;background:#fff;box-shadow:0 1px 6px rgba(0,0,0,.15);text-align:center;padding-top:20px}
.card .pic{width:150px;height:110px;margin:0 auto;background:linear-gradient(180deg,#f2f2f2,#d9d9d9);border-radius:4px}
.card h3{margin-top:22px;font-size:15px;font-weight:700;color:#222}
.card p{margin-top:10px;font-size:14px;line-height:24px;color:var(--muted);padding:0 14px}
.card a{display:inline-block;margin-top:8px;font-size:11.5px;font-weight:700;color:var(--red);text-decoration:underline}

.g1{left:0;top:1972px;width:727px;height:398px;background:radial-gradient(ellipse at 55% 65%,#b8875a 0%,#5b3a26 35%,#1e1a1a 80%)}
.g2{left:0;top:2379px;width:391px;height:209px;background:radial-gradient(ellipse at 30% 50%,#a7794a 0%,#35404e 55%,#1d2532 100%)}
.g3{left:400px;top:2379px;width:327px;height:209px;background:radial-gradient(ellipse at 50% 55%,#e1b06a 0%,#7a4a36 35%,#2a1f2a 85%)}
.g4{left:736px;top:1972px;width:464px;height:227px;background:radial-gradient(ellipse at 55% 60%,#b99b7b 0%,#5c5e64 45%,#2d3038 100%)}
.g5{left:736px;top:2208px;width:464px;height:380px;background:radial-gradient(ellipse at 50% 55%,#8e7e6c 0%,#3f4c58 45%,#1f2a35 100%)}

.tcard{top:2785px;width:477px;height:238px;background:#fff;box-shadow:0 1px 7px rgba(0,0,0,.15);text-align:center}
.tcard .avatar{position:absolute;left:200px;top:-38px;width:76px;height:76px;border-radius:50%;background:linear-gradient(180deg,#c9ced6,#8a93a0);border:3px solid #fff;box-shadow:0 1px 5px rgba(0,0,0,.3)}
.tcard .quote{position:absolute;right:18px;top:-14px;font-family:"Poppins",sans-serif;font-weight:700;font-size:56px;line-height:56px;color:var(--red)}
.tcard p{margin-top:65px;padding:0 48px;font-size:14px;line-height:27px;color:var(--muted)}
.tcard .who{margin-top:10px;font-size:14px;color:#222}
.tcard .who span{color:var(--muted)}
.tcard .stars{margin-top:10px;color:#f3b300;font-size:13px;letter-spacing:1px}
.dots{left:572px;top:3083px;display:flex;gap:3px}
.dots span{width:9px;height:9px;border-radius:50%;background:#777}
.dots span.off{background:#fff;border:1px solid #777}

.contact{left:0;top:3167px;width:1200px;height:441px;background:linear-gradient(180deg,#e8132d,#d80f27)}
.contact h2{left:0;top:50px;width:1200px;text-align:center;font-family:"Poppins",sans-serif;font-weight:600;font-size:38px;color:#fff}
.field{background:#fff;border:1px solid #ddd;font-size:14.5px;color:#777;padding:14px 13px}
.contact .btn{left:519px;top:326px;width:162px;height:51px;justify-content:center;background:#9b1423;font-size:13.5px}

.footer{left:0;top:3608px;width:1200px;height:322px;background:var(--footer);color:#fff;font-size:13.5px}
.footer h4{font-size:15px;font-weight:700;text-decoration:underline;color:#fff}
.flist{display:flex;flex-direction:column;gap:21px;margin-top:26px}
.flist div{display:flex;align-items:center;gap:21px}
.fbrand{left:860px;top:143px;display:flex;align-items:center;gap:10px;font-family:"Poppins",sans-serif;font-weight:600;font-size:17px;color:#9a9a9a}
.fbrand i{width:20px;height:20px;background:#9a9a9a;display:block}
.copy{left:0;top:3930px;width:1200px;height:46px;background:var(--footer-deep);color:#fff;font-size:13.5px;text-align:center;line-height:46px}
</style>
</head>
<body>

<header class="abs topbar">
  <div class="abs social"><span></span><span></span><span></span><span></span></div>
  <div class="abs phone">
    <svg width="14" height="14" viewBox="0 0 24 24"><path fill="#fff" d="M6.6 10.8a15 15 0 006.6 6.6l2.2-2.2a1 1 0 011-.25 11.4 11.4 0 003.6.6 1 1 0 011 1V20a1 1 0 01-1 1A17 17 0 013 4a1 1 0 011-1h3.5a1 1 0 011 1c0 1.25.2 2.45.6 3.6a1 1 0 01-.25 1z"/></svg>
    49 2100 300-7
  </div>
  <nav class="abs links"><span>CAREER</span><span>CONTACT</span><span>DOWNLOADS</span><span>IMPRINT</span></nav>
</header>

<div class="abs nav">
  <div class="abs brand"><i></i>BEAMFORGE MACHINE WORKS</div>
  <nav class="abs menu"><span class="on">HOME</span><span>PICTURES</span><span>MACHINES FOR SALE</span><span>ABOUT</span><span>CONTACT</span></nav>
  <div class="abs search"><svg width="18" height="18" viewBox="0 0 24 24"><circle cx="10" cy="10" r="6.5" fill="none" stroke="#fff" stroke-width="3"/><path d="M15 15l6 6" stroke="#fff" stroke-width="3.5" stroke-linecap="round"/></svg></div>
</div>

<section class="abs hero" role="img" aria-label="Laser cutting head throwing bright sparks across a metal sheet">
  <h1 class="abs">BEAMFORGE<br>MACHINE WORKS</h1>
  <p class="abs">Sed ut perspiciatis unde omnis iste natus error sit voluptatem accusantium doloremque laudantium, totam rem aperiam, eaque ipsa quae ab illo inventore</p>
  <a class="abs btn">GET STARTED
    <svg width="14" height="14" viewBox="0 0 24 24"><circle cx="12" cy="12" r="11" fill="#fff"/><path d="M10 7l5 5-5 5" stroke="#e4132b" stroke-width="3" fill="none"/></svg></a>
</section>

<h2 class="abs about-title">ABOUT US</h2>
<p class="abs about-lead">Lorem ipsum dolor sit amet, consectetur adipiscing elit, sed do eiusmod tempor incididunt ut labore et dolore magna aliqua. Lorem ipsum dolor sit amet</p>
<p class="abs about-body">Sed ut perspiciatis unde omnis iste natus error sit voluptatem accusantium doloremque laudantium, totam rem aperiam, eaque ipsa quae ab illo inventore veritatis et quasi architecto beatae vitae dicta sunt explicabo. Nemo enim ipsam voluptatem quia voluptas sit aspernatur aut odit aut fugit, sed quia consequuntur magni dolores eos qui ratione voluptatem sequi nesciunt. Neque porro quisquam est, qui dolorem ipsum quia dolor sit amet, consectetur, adipisci velit, sed quia non numquam eius modi</p>
<div class="abs photo ph1" role="img" aria-label="Close view of a laser nozzle cutting steel with sparks"></div>
<div class="abs photo ph2" role="img" aria-label="Laser head cutting a grid pattern into a metal plate"></div>

<h2 class="abs section-title" style="top:1420px">MACHINES FOR SALE</h2>
<p class="abs section-lead" style="top:1490px">Lorem ipsum dolor sit amet, consectetur adipiscing elit, sed do eiusmod tempor incididunt ut labore et dolore magna aliqua. Ut enim ad minim veniam, quis nostrud exercitation ullamco.</p>
<div class="abs cards">
  <div class="card"><div class="pic" role="img" aria-label="Desktop laser engraving machine"></div><h3>PRODUCT TITLE</h3><p>Sed ut perspiciatis unde omnis iste natus error sit voluptatem</p><a>LEARN MORE</a></div>
  <div class="card"><div class="pic" role="img" aria-label="Laser cutting head module"></div><h3>PRODUCT TITLE</h3><p>Sed ut perspiciatis unde omnis iste natus error sit voluptatem</p><a>LEARN MORE</a></div>
  <div class="card"><div class="pic" role="img" aria-label="Flatbed CNC laser cutting table"></div><h3>PRODUCT TITLE</h3><p>Sed ut perspiciatis unde omnis iste natus error sit voluptatem</p><a>LEARN MORE</a></div>
  <div class="card"><div class="pic" role="img" aria-label="Desktop laser engraving machine"></div><h3>PRODUCT TITLE</h3><p>Sed ut perspiciatis unde omnis iste natus error sit voluptatem</p><a>LEARN MORE</a></div>
</div>

<div class="abs g1" role="img" aria-label="Laser cutter head sending sparks over a workpiece"></div>
<div class="abs g2" role="img" aria-label="Laser cutting through a slotted metal plate"></div>
<div class="abs g3" role="img" aria-label="Sparks spraying beneath a laser nozzle"></div>
<div class="abs g4" role="img" aria-label="Laser head over a reflective metal sheet"></div>
<div class="abs g5" role="img" aria-label="Angled laser head cutting steel in blue light"></div>

<h2 class="abs section-title" style="top:2660px">TESTIMONIALS</h2>
<div class="abs tcard" style="left:111px">
  <div class="avatar" role="img" aria-label="Client portrait"></div><div class="quote">”</div>
  <p>At vero eos et accusamus et iusto odio dignissimos ducim us qui blanditiis praesentium voluptatum deleniti atque corrupti quos dolores et quas molestias excepturi sint.</p>
  <div class="who">DANIEL REEVE <span>, Businessman</span></div><div class="stars">★★★★★</div>
</div>
<div class="abs tcard" style="left:611px">
  <div class="avatar" role="img" aria-label="Client portrait"></div><div class="quote">”</div>
  <p>At vero eos et accusamus et iusto odio dignissimos ducim us qui blanditiis praesentium voluptatum deleniti atque corrupti quos dolores et quas molestias excepturi sint.</p>
  <div class="who">DANIEL REEVE <span>, Businessman</span></div><div class="stars">★★★★★</div>
</div>
<div class="abs dots"><span></span><span></span><span class="off"></span><span></span><span></span></div>

<section class="abs contact">
  <h2 class="abs">CONTACT US</h2>
  <div class="abs field" style="left:116px;top:145px;width:236px;height:51px">First Name</div>
  <div class="abs field" style="left:360px;top:145px;width:236px;height:51px">Email Address</div>
  <div class="abs field" style="left:604px;top:145px;width:236px;height:51px">Phone No</div>
  <div class="abs field" style="left:848px;top:145px;width:236px;height:51px">Address</div>
  <div class="abs field" style="left:119px;top:207px;width:963px;height:85px">Message</div>
  <a class="abs btn">SUBMIT NOW
    <svg width="14" height="14" viewBox="0 0 24 24"><circle cx="12" cy="12" r="11" fill="#fff"/><path d="M10 7l5 5-5 5" stroke="#9b1423" stroke-width="3" fill="none"/></svg></a>
</section>

<footer class="abs footer">
  <div class="abs" style="left:113px;top:58px">
    <h4>FIND US ON</h4>
    <div class="flist" style="gap:18px">
      <div><svg width="10" height="14" viewBox="0 0 10 14"><path fill="#fff" d="M5 0a5 5 0 015 5c0 4-5 9-5 9S0 9 0 5a5 5 0 015-5zm0 3a2 2 0 100 4 2 2 0 000-4z"/></svg>520 Lorem Ipsum Dolor</div>
      <div style="padding-left:31px">United States</div>
      <div><svg width="12" height="12" viewBox="0 0 24 24"><path fill="#fff" d="M6.6 10.8a15 15 0 006.6 6.6l2.2-2.2a1 1 0 011-.25 11.4 11.4 0 003.6.6 1 1 0 011 1V20a1 1 0 01-1 1A17 17 0 013 4a1 1 0 011-1h3.5a1 1 0 011 1c0 1.25.2 2.45.6 3.6a1 1 0 01-.25 1z"/></svg>1 888 888 888</div>
      <div><svg width="14" height="11" viewBox="0 0 14 11"><rect x=".7" y=".7" width="12.6" height="9.6" fill="none" stroke="#fff" stroke-width="1.4"/><path d="M1 1l6 5 6-5" fill="none" stroke="#fff" stroke-width="1.4"/></svg>info@beamforgeworks.com</div>
    </div>
  </div>
  <div class="abs" style="left:432px;top:58px">
    <h4>QUICK LINKS</h4>
    <div class="flist"><div>»<span>Home</span></div><div>»<span>About Us</span></div><div>»<span>Machines for sale</span></div><div>»<span>Reviews</span></div><div>»<span>Resources</span></div></div>
  </div>
  <div class="abs" style="left:658px;top:58px">
    <h4>OTHER LINKS</h4>
    <div class="flist"><div>»<span>FAQ</span></div><div>»<span>Help Service</span></div><div>»<span>Terms &amp; Conditions</span></div><div>»<span>Privacy Policy</span></div><div>»<span>Machines</span></div></div>
  </div>
  <div class="abs fbrand"><i></i>BEAMFORGE</div>
</footer>
<div class="abs copy">© 2020 Beamforge Machine Works. All Rights Reserved</div>

</body>
</html>
```